Lighting Wholesaler

As our company name is Brenmore Lighting we prefer a Castle as the photo of image, we want a plain glossy plain white back ground, all print to be in black however the company slogan "We Only Wholesale To Projects" to be in blue print, please see attached files to see what we want, This business card is for Darren Hollow and NOT FOR Tom Pardew

Industry/Entity Type

Business

Contact Information for Business Card

Brenmore Lighting Pty Ltd ABN 51 627 913 480
We Only Wholesale To Projects (blue print see attachment)
Darren Hollow
Unit 9, 27 Wattle Rd., Blacktown NSW 2148
Website : www.brenmorelighting-example.com.au
Email : sales@brenmorelighting-example.com.au
Ph : 0491 572 806 Fax : 9812 3059

On Reverse Side as per attachment
Intercoms - Video Audio
Home Security Systems
Commercial Lighting
Domestic Lighting
Fluorescent Lighting
Emergency Lighting
Ventilation Solutions
Exhaust Fan Systems
Xmas Tree Stands (blue print see attachment)

Requirements
Must have
• The business card must be flexible, what I need is a system that will allow me to create using this same template for other people, e.g. this card is for Darren Hollow however we have others in the company and so we will need to change the name, the phone number and the email address of that person. The attached design of my business Card (Tom Pardew) is a layout that I am extremely happy with as it is not congested and it is easy to read but your logo photo may be differrent, if you can find a nicer photo it will be better

```html
<!DOCTYPE html>
<html lang="en">
<head>
<meta charset="utf-8">
<title>Brenmore Lighting – Business Card</title>
<link rel="stylesheet" href="https://fonts.googleapis.com/css2?family=Tinos:ital,wght@0,400;0,700;1,400;1,700&display=swap">
<style>
  :root {
    --ink: #111111;
    --paper: #ffffff;
    --slogan-blue: #3a4fa8;
    --swoosh-grey: #8a8a8a;
    --swoosh-grey-light: #c9c9c9;
    --card-edge: #3a3a3a;
  }
  * { box-sizing: border-box; margin: 0; padding: 0; }
  html, body { width: 1200px; height: 983px; overflow: hidden; background: var(--paper); }
  body { position: relative; font-family: "Tinos", "Times New Roman", serif; color: var(--ink); }

  .card { position: absolute; background: var(--paper); border: 1.5px solid var(--card-edge); overflow: hidden; }
  .card__swoosh { position: absolute; left: 0; top: 0; width: 100%; height: 100%; }

  /* Reverse side */
  .card--back { left: 15px; top: 12px; width: 420px; height: 699px; }
  .card--back .card__header {
    position: absolute; left: 0; top: 0; width: 100%; height: 283px; background: var(--ink);
  }
  .card--back .brand { position: absolute; left: 0; top: 92px; width: 100%; display: flex; flex-direction: column; align-items: center; }
  .card--back .brand__row { display: flex; align-items: center; gap: 10px; }
  .card--back .brand__mark { width: 34px; height: 34px; background: var(--paper); }
  .card--back .brand__name { color: var(--paper); font-size: 33px; font-weight: 700; line-height: 1; }
  .card--back .brand__rule { width: 340px; height: 2px; background: var(--paper); margin-top: 4px; }
  .card--back .brand__meta { width: 340px; display: flex; justify-content: space-between; color: var(--paper); font-size: 9px; margin-top: 2px; padding-left: 60px; }
  .card--back .slogan { position: absolute; left: 0; top: 166px; width: 100%; text-align: center; }

  .slogan { color: var(--slogan-blue); font-style: italic; font-weight: 700; font-size: 19px; letter-spacing: 0.3px; }

  .service-list { position: absolute; left: 84px; top: 322px; list-style: none; }
  .service-list li { display: flex; align-items: center; gap: 9px; font-size: 19px; font-weight: 700; height: 31.5px; }
  .service-list .bulb { width: 13px; height: 17px; flex: none; }

  /* Front side */
  .card--front { left: 457px; top: 12px; width: 700px; height: 418px; }
  .card--front .brand { position: absolute; left: 20px; top: 40px; width: 345px; }
  .card--front .brand__row { display: flex; align-items: center; gap: 10px; }
  .card--front .brand__mark { width: 36px; height: 36px; background: var(--ink); }
  .card--front .brand__name { font-size: 33px; font-weight: 700; line-height: 1; }
  .card--front .brand__rule { height: 2.5px; background: var(--ink); margin-top: 5px; }
  .card--front .brand__meta { display: flex; justify-content: space-between; font-size: 9px; margin-top: 2px; padding-left: 80px; }
  .card--front .slogan { position: absolute; left: 20px; top: 122px; }

  .contact { position: absolute; left: 40px; top: 228px; z-index: 1; }
  .contact__name { font-size: 19px; font-weight: 700; line-height: 24px; }
  .contact__line { font-size: 14px; font-weight: 700; line-height: 20px; }
</style>
</head>
<body>

  <section class="card card--back" aria-label="Business card reverse side">
    <div class="card__header"></div>
    <div class="brand">
      <div class="brand__row">
        <span class="brand__mark"></span>
        <span class="brand__name">Brenmore Lighting</span>
      </div>
      <div class="brand__rule"></div>
      <div class="brand__meta"><span>ABN 51 627 913 480</span><span>PTY.LTD</span></div>
    </div>
    <p class="slogan">"We Only Wholesale To Projects"</p>

    <ul class="service-list">
      <li><svg class="bulb" viewBox="0 0 13 17"><circle cx="6.5" cy="6" r="5" fill="none" stroke="#111" stroke-width="1.3"/><rect x="4" y="11.5" width="5" height="4" fill="#111"/></svg>Intercoms - Video Audio</li>
      <li><svg class="bulb" viewBox="0 0 13 17"><circle cx="6.5" cy="6" r="5" fill="none" stroke="#111" stroke-width="1.3"/><rect x="4" y="11.5" width="5" height="4" fill="#111"/></svg>Home Security Systems</li>
      <li><svg class="bulb" viewBox="0 0 13 17"><circle cx="6.5" cy="6" r="5" fill="none" stroke="#111" stroke-width="1.3"/><rect x="4" y="11.5" width="5" height="4" fill="#111"/></svg>Commercial Lighting</li>
      <li><svg class="bulb" viewBox="0 0 13 17"><circle cx="6.5" cy="6" r="5" fill="none" stroke="#111" stroke-width="1.3"/><rect x="4" y="11.5" width="5" height="4" fill="#111"/></svg>Domestic Lighting</li>
      <li><svg class="bulb" viewBox="0 0 13 17"><circle cx="6.5" cy="6" r="5" fill="none" stroke="#111" stroke-width="1.3"/><rect x="4" y="11.5" width="5" height="4" fill="#111"/></svg>Fluorescent Lighting</li>
      <li><svg class="bulb" viewBox="0 0 13 17"><circle cx="6.5" cy="6" r="5" fill="none" stroke="#111" stroke-width="1.3"/><rect x="4" y="11.5" width="5" height="4" fill="#111"/></svg>Emergency Lighting</li>
      <li><svg class="bulb" viewBox="0 0 13 17"><circle cx="6.5" cy="6" r="5" fill="none" stroke="#111" stroke-width="1.3"/><rect x="4" y="11.5" width="5" height="4" fill="#111"/></svg>Ventilation Solutions</li>
      <li><svg class="bulb" viewBox="0 0 13 17"><circle cx="6.5" cy="6" r="5" fill="none" stroke="#111" stroke-width="1.3"/><rect x="4" y="11.5" width="5" height="4" fill="#111"/></svg>Exhaust Fan Systems</li>
      <li><svg class="bulb" viewBox="0 0 13 17"><circle cx="6.5" cy="6" r="5" fill="none" stroke="#111" stroke-width="1.3"/><rect x="4" y="11.5" width="5" height="4" fill="#111"/></svg>Xmas Tree Stands</li>
    </ul>

    <svg class="card__swoosh" viewBox="0 0 420 699" preserveAspectRatio="none" aria-hidden="true">
      <defs>
        <linearGradient id="backGrey" x1="0" y1="0" x2="1" y2="0">
          <stop offset="0" stop-color="#c9c9c9"/>
          <stop offset="1" stop-color="#7a7a7a"/>
        </linearGradient>
      </defs>
      <path d="M0 662 C150 655 320 620 420 560 L420 615 C300 648 150 664 0 668 Z" fill="url(#backGrey)"/>
      <path d="M0 668 C150 664 300 648 420 615 L420 699 L0 699 Z" fill="#111"/>
    </svg>
  </section>

  <section class="card card--front" aria-label="Business card front side">
    <div class="brand">
      <div class="brand__row">
        <span class="brand__mark"></span>
        <span class="brand__name">Brenmore Lighting</span>
      </div>
      <div class="brand__rule"></div>
      <div class="brand__meta"><span>ABN 51 627 913 480</span><span>PTY.LTD</span></div>
    </div>
    <p class="slogan">"We Only Wholesale To Projects"</p>

    <svg class="card__swoosh" viewBox="0 0 700 418" preserveAspectRatio="none" aria-hidden="true">
      <defs>
        <linearGradient id="frontGrey" x1="0" y1="0" x2="1" y2="0">
          <stop offset="0" stop-color="#d4d4d4"/>
          <stop offset="1" stop-color="#7a7a7a"/>
        </linearGradient>
      </defs>
      <path d="M0 366 C300 364 520 335 700 262 L700 305 C500 350 250 372 0 374 Z" fill="url(#frontGrey)"/>
      <path d="M0 374 C250 372 500 350 700 305 L700 418 L0 418 Z" fill="#111"/>
    </svg>

    <div class="contact">
      <p class="contact__name">Darren Hollow</p>
      <p class="contact__line">Unit 9, 27 Wattle Rd., Blacktown NSW 2148</p>
      <p class="contact__line">Website : www.brenmorelighting-example.com.au</p>
      <p class="contact__line">Email : sales@brenmorelighting-example.com.au</p>
      <p class="contact__line">Ph : 0491 572 806</p>
      <p class="contact__line">Fax : 9812 3059</p>
    </div>
  </section>

</body>
</html>
```